Multiple Packaging Solutions for LED bulbs

We need a packaging design for led bulbs for our company. We need something that can be easily adjusted in different packaging types, as we have multiple different products. It needs to be fresh, friendly, happy but at the same time corporate. We provide some basic packaging dimensions and also our logo in the respective files. The packaging could be of plastic/trasparent, or carton (regular or ecofriendly)

It Company

```html
<!DOCTYPE html>
<html lang="en">
<head>
<meta charset="utf-8">
<title>lumora — LED Panel Packaging</title>
<link rel="stylesheet" href="https://fonts.googleapis.com/css2?family=Titillium+Web:wght@300;400;600&display=swap">
<style>
  :root {
    --canvas-bg: #e4e4e6;
    --purple-deep: #2f2862;
    --purple: #3e3574;
    --purple-light: #5b5089;
    --white: #ffffff;
    --magenta: #c8346e;
    --orange: #f39323;
    --coral: #e9604a;
    --font-main: "Titillium Web", Arial, sans-serif;
  }
  * { margin: 0; padding: 0; box-sizing: border-box; }
  html, body {
    width: 1200px; height: 960px; overflow: hidden;
    background: var(--canvas-bg);
    font-family: var(--font-main);
  }
  .dieline {
    position: absolute; left: 150px; top: 180px;
    display: flex; height: 600px;
  }
  .panel {
    position: relative; height: 100%; overflow: hidden;
    background: linear-gradient(160deg, var(--purple-deep) 0%, var(--purple) 55%, var(--purple-light) 100%);
    border-right: 1px solid rgba(255,255,255,0.08);
  }
  .panel--wide { width: 300px; }
  .panel--narrow { width: 150px; }

  .brand {
    position: absolute; display: flex; align-items: center; gap: 10px;
    color: var(--white); font-weight: 300; letter-spacing: 0.5px;
  }
  .brand__dot {
    width: 22px; height: 22px; border-radius: 50%;
    background: var(--orange);
  }
  .brand--small { top: 46px; left: 34px; font-size: 26px; }
  .brand--back { top: 96px; right: 34px; font-size: 30px; }

  .vertical-name {
    position: absolute; color: var(--white); font-weight: 300;
    writing-mode: vertical-rl; white-space: nowrap; line-height: 1;
  }
  .vertical-name--front { left: 28px; top: 300px; font-size: 76px; }
  .vertical-name--back { left: 26px; top: 300px; font-size: 64px; }
  .vertical-name--side { right: 22px; top: 330px; font-size: 24px; }

  .motif-area {
    position: absolute; border-radius: 18px;
    background: linear-gradient(180deg, rgba(255,255,255,0.18), rgba(243,147,35,0.18));
  }
  .motif-area--front { left: 120px; top: 90px; width: 170px; height: 460px; }
  .motif-area--side { left: 0; top: 90px; width: 90px; height: 460px; }

  .specs {
    position: absolute; left: 120px; top: 300px;
    color: var(--magenta); font-size: 16px; font-weight: 400; line-height: 1.18;
    list-style: none;
  }
  .marks {
    position: absolute; left: 120px; bottom: 40px; display: flex; gap: 10px;
  }
  .marks span {
    width: 20px; height: 20px; border-radius: 50%; background: var(--magenta);
  }
</style>
</head>
<body>
  <main class="dieline">
    <section class="panel panel--wide front-panel">
      <div class="brand brand--small"><span class="brand__dot"></span>lumora</div>
      <div class="motif-area motif-area--front" role="img" aria-label="Large outlined light bulb brand motif"></div>
      <div class="vertical-name vertical-name--front">lumora</div>
    </section>

    <section class="panel panel--narrow side-panel">
      <div class="motif-area motif-area--side" role="img" aria-label="Orange bulb brand motif continuing from the front"></div>
      <div class="vertical-name vertical-name--side">lumora</div>
    </section>

    <section class="panel panel--wide back-panel">
      <div class="brand brand--back"><span class="brand__dot"></span>lumora</div>
      <div class="vertical-name vertical-name--back">lumora</div>
      <ul class="specs">
        <li>LM-PNL-3030W</li>
        <li>LED Panel</li>
        <li>Size: 296x296mm</li>
        <li>Wattage: 30W</li>
        <li>CCT: 3000K</li>
        <li>Voltage: 100-240VAC</li>
        <li>CRI&gt;80</li>
      </ul>
      <div class="marks" aria-label="Disposal and certification marks">
        <span></span><span></span><span></span><span></span>
      </div>
    </section>

    <section class="panel panel--narrow side-panel">
      <div class="vertical-name vertical-name--side">lumora</div>
    </section>
  </main>
</body>
</html>
```